Animated (HTML5) banner ad for fantasy football (soccer) app

We want to promote our app where users can:
- Create your fantasy team
- Get points when your players score in real life
- Challenge your friends in private competitions
- Select players from many different leagues: Titan Series, Summit Circuit, Vértix, Kampfrunde, Coppa Brio, Trophée 7, Meridian Trophy, ++
Please have a look here for screenshots and color palette: https://www.plandeck.example/file/Xk93mQpL2vRtZaWbNcEdHf/Video?node-id=0%3A1
Sizes:
1:1 (Square) - 1200 x 1200 pixels.
1.91:1 (Landscape) – 1200 x 628 pixels.
4:5 (Portrait) – 1200 x 1500 pixels.
Prefer the file to be in Google Web Designer, but other might work too.

```html
<!DOCTYPE html>
<html lang="en">
<head>
<meta charset="utf-8">
<title>GOALCREST – Manage Your Dream Team</title>
<link rel="stylesheet" href="https://fonts.googleapis.com/css2?family=Montserrat:wght@700;800;900&family=Luckiest+Guy&display=swap">
<style>
  :root {
    --sky-top: #4a3f3a;
    --sky-mid: #8a6a6a;
    --stands: #b4514f;
    --glow: #7fd6c4;
    --pitch: #c8b84a;
    --pitch-low: #b9a63a;
    --white: #ffffff;
    --cta-bg: #6ef5e0;
    --cta-text: #5b6a62;
    --arrow: #eef514;
    --soccer-shadow: #8a2e10;
    --soccer-edge: #f4c430;
  }
  * { margin: 0; padding: 0; box-sizing: border-box; }
  html, body { width: 1200px; height: 1200px; overflow: hidden; background: var(--sky-top); }
  .banner {
    position: relative;
    width: 1200px;
    height: 1200px;
    overflow: hidden;
    font-family: "Montserrat", Arial, sans-serif;
    color: var(--white);
  }
  .stadium-scene {
    position: absolute;
    inset: 0;
    background:
      radial-gradient(circle at 600px 470px, rgba(240,236,255,0.95) 0 190px, rgba(127,214,196,0.55) 215px, rgba(127,214,196,0) 330px),
      linear-gradient(180deg, var(--sky-top) 0%, var(--sky-mid) 35%, #a88a7e 52%, var(--stands) 68%, #c0705a 78%, var(--pitch) 90%, var(--pitch-low) 100%);
  }
  .brand-name {
    position: absolute;
    top: 110px;
    left: 0;
    width: 100%;
    text-align: center;
    font-weight: 900;
    font-size: 120px;
    letter-spacing: 2px;
    color: var(--white);
  }
  .sport-word {
    position: absolute;
    left: 190px;
    top: 520px;
    font-family: "Luckiest Guy", "Arial Black", sans-serif;
    font-size: 190px;
    line-height: 1;
    transform: rotate(-14deg);
    transform-origin: left bottom;
    background: linear-gradient(90deg, #f23a1e 0%, #e83a6e 22%, #b84ad8 48%, #a27ef0 70%, #a9ecec 100%);
    -webkit-background-clip: text;
    background-clip: text;
    color: transparent;
    filter: drop-shadow(6px 6px 0 var(--soccer-shadow)) drop-shadow(1px 1px 0 var(--soccer-edge));
  }
  .headline {
    position: absolute;
    left: 0;
    width: 100%;
    text-align: center;
    font-weight: 800;
    line-height: 1;
  }
  .headline-lead { top: 790px; font-size: 62px; }
  .headline-main { top: 850px; font-size: 106px; letter-spacing: 1px; }
  .features {
    position: absolute;
    top: 960px;
    left: 60px;
    width: 1080px;
    text-align: center;
    font-weight: 800;
    font-size: 20px;
    line-height: 26px;
    text-transform: uppercase;
  }
  .cta-row {
    position: absolute;
    top: 1065px;
    left: 0;
    width: 100%;
    height: 98px;
  }
  .cta-arrows { position: absolute; top: 0; }
  .cta-arrows.left { left: 200px; }
  .cta-arrows.right { left: 780px; }
  .cta-button {
    position: absolute;
    left: 437px;
    width: 328px;
    height: 98px;
    border-radius: 8px;
    background: var(--cta-bg);
    box-shadow: inset 0 0 0 3px rgba(255,255,255,0.5);
    text-align: center;
    font-weight: 900;
    font-size: 74px;
    line-height: 98px;
    color: var(--cta-text);
    -webkit-text-stroke: 2px var(--white);
    paint-order: stroke fill;
  }
</style>
</head>
<body>
<main class="banner">
  <div class="stadium-scene" role="img" aria-label="Illustration of a glowing soccer ball flying over a floodlit stadium at night"></div>

  <div class="brand-name">GOALCREST</div>

  <div class="sport-word">SOCCER</div>

  <h1 class="headline headline-lead">MANAGE YOUR</h1>
  <h2 class="headline headline-main">DREAM TEAM</h2>

  <p class="features">
    Create your fantasy team | Get points when your players score in real life<br>
    Challenge your friends in private competitions &nbsp;|&nbsp; Select players from many<br>
    different leagues
  </p>

  <div class="cta-row">
    <svg class="cta-arrows left" width="220" height="98" viewBox="0 0 220 98" aria-hidden="true">
      <polygon points="5,26 45,49 5,72" fill="var(--arrow)"/>
      <polygon points="70,20 125,49 70,78" fill="var(--arrow)"/>
      <polygon points="148,13 215,49 148,85" fill="var(--arrow)"/>
    </svg>
    <div class="cta-button">PLAY</div>
    <svg class="cta-arrows right" width="220" height="98" viewBox="0 0 220 98" aria-hidden="true">
      <polygon points="72,13 5,49 72,85" fill="var(--arrow)"/>
      <polygon points="150,20 95,49 150,78" fill="var(--arrow)"/>
      <polygon points="215,26 175,49 215,72" fill="var(--arrow)"/>
    </svg>
  </div>
</main>
</body>
</html>
```